Business Card Design for Telecommunications and IT Solutions company "OKRA"

BC for telecommunications company name "OKRA" with slogan "Telecom & IT Solutions"

should have the full name as above "OKRA" and the slogan
color reqiured black, red (dark) and white

simple, professional, serious, modern design is required

1 side of business card have a full details, contacts and logo
other side have only the logo, website and full company name "ALOKRA Company for Telecommunications service & Information Technology LLC"

i have attached the logo and current business card sample and note that the logo was changed not the same in the attached business card

Industry/Entity Type

Telecommunications

Contact Information for Business Card

Full name: Omar Nabil Al Hudari
Job title: General Manager
Mobile no: +964xxxxxxxxx
email: omar@okra-tel.example
full name of the company: ALOKRA Company Telecommunications Services & Information Technology LLC.
website: www.okra-tel.example
address: Nakheel Dist. 148/7 JubailaQadim, Basra, Iraq

Requirements
Must have
• two languages in the same side of business card (English, Arabic) for only the name and title

```html
<!DOCTYPE html>
<html lang="en">
<head>
<meta charset="utf-8">
<title>OKRA Business Card</title>
<link rel="stylesheet" href="https://fonts.googleapis.com/css2?family=Open+Sans:wght@400;600;700&family=Crimson+Text:ital@1&family=Tajawal:wght@400;700&display=swap">
<style>
  :root {
    --backdrop: #d6d7d9;
    --paper: #ffffff;
    --brand-red: #9a1b1f;
    --mark-red: #c8171e;
    --ink-black: #231f20;
    --text-dark: #1a1a1a;
    --text-light: #ffffff;
  }
  html, body {
    margin: 0;
    width: 1200px;
    height: 1000px;
    overflow: hidden;
    background: var(--backdrop);
  }
  .business-card {
    position: absolute;
    left: 56px;
    top: 173px;
    width: 1091px;
    height: 655px;
    background: var(--paper);
    box-shadow: 0 3px 10px rgba(0,0,0,0.35);
    overflow: hidden;
  }
  .brand-area {
    position: absolute;
    left: 0; top: 0;
    width: 100%; height: 357px;
  }
  .brand-lockup {
    position: absolute;
    left: 400px;
    top: 128px;
    display: flex;
    align-items: center;
    gap: 18px;
  }
  .brand-dot {
    width: 44px; height: 44px;
    border-radius: 50%;
    background: var(--mark-red);
  }
  .brand-name {
    font-family: "Open Sans", sans-serif;
    font-weight: 700;
    font-size: 92px;
    line-height: 1;
    color: var(--mark-red);
    letter-spacing: 2px;
  }
  .brand-slogan {
    position: absolute;
    left: 279px;
    top: 248px;
    font-family: "Crimson Text", serif;
    font-style: italic;
    font-size: 24px;
    color: var(--text-dark);
    letter-spacing: 0.5px;
  }
  .company-band {
    position: absolute;
    left: 0; top: 357px;
    width: 100%; height: 200px;
    background: var(--brand-red);
    color: var(--text-light);
  }
  .company-en {
    position: absolute;
    left: 54px; top: 44px;
    font-family: "Open Sans", sans-serif;
  }
  .company-en .company-title {
    margin: 0 0 4px;
    font-size: 33px;
    font-weight: 700;
    line-height: 1.15;
  }
  .company-en .company-desc {
    margin: 0;
    font-size: 24px;
    font-weight: 400;
    line-height: 31px;
  }
  .company-ar {
    position: absolute;
    right: 45px; top: 40px;
    direction: rtl;
    text-align: right;
    font-family: "Tajawal", sans-serif;
  }
  .company-ar .company-title {
    margin: 0 0 2px;
    font-size: 36px;
    font-weight: 700;
    line-height: 1.15;
  }
  .company-ar .company-desc {
    margin: 0;
    font-size: 28px;
    font-weight: 400;
    line-height: 32px;
  }
  .web-band {
    position: absolute;
    left: 0; top: 557px;
    width: 100%; height: 98px;
    background: var(--ink-black);
    display: flex;
    align-items: center;
    justify-content: center;
  }
  .website {
    font-family: "Open Sans", sans-serif;
    font-size: 40px;
    font-weight: 400;
    color: var(--text-light);
    margin-top: -8px;
  }
</style>
</head>
<body>
  <div class="business-card">
    <section class="brand-area">
      <div class="brand-lockup">
        <span class="brand-name">OKRA</span>
        <span class="brand-dot"></span>
      </div>
      <div class="brand-slogan">Telecom &amp; IT Solutions</div>
    </section>

    <section class="company-band">
      <div class="company-en">
        <p class="company-title">ALOKRA Company</p>
        <p class="company-desc">Telecommunications Services<br>&amp; Information Technology LTD.</p>
      </div>
      <div class="company-ar" lang="ar">
        <p class="company-title">شركة أوكرا</p>
        <p class="company-desc">خدمات الإتصالات وتقنية<br>المعلومات المحدودة</p>
      </div>
    </section>

    <footer class="web-band">
      <span class="website">www.okra-tel.example</span>
    </footer>
  </div>
</body>
</html>
```